Graniteway Surface Works, Inc. Business Card

New business, we do epoxy, polishing concrete, underlayment, fluid applied flooring, sound proofing, double sided, will need 3 sets of cards with 3 different names and phone numbers.
Company: Graniteway Surface Works, Inc.
Address and Phone: 6339 Charlotte Pike PMB 2183Nashville, TN 38514
(615) 418-3927
www.granitewaysurfaceworks.example

Target Market(s)

General Contractors, Contractors, Architects

Contact Information for Business Card

1st Card: Devon Halvorsen C. 708.214.5873 e. devon@granitewaysurfaceworks.example
Vice President
2nd Card: Morgan Prescoe C. 708.389.6145 e. morgan@granitewaysurfaceworks.example
President
3rd Card: Bo Vu C. 405.631.8207 e. bo@granitewaysurfaceworks.example
Managing Partner

Font styles to use
Serif
Sans Serif

Requirements
Must have
• Professional Clean Design, Implement colors from Logo or nicely contrasting
Nice to have
• N/A

```html
<!DOCTYPE html>
<html lang="en">
<head>
<meta charset="utf-8">
<title>Graniteway Surface Works – Business Card Concepts</title>
<link href="https://fonts.googleapis.com/css2?family=Jost:wght@500&family=Montserrat:wght@500;600;700&family=Saira+Semi+Condensed:wght@600&display=swap" rel="stylesheet">
<style>
  :root {
    --board: #b9b9b9;
    --card: #f4f4f6;
    --blue: #0a63b4;
    --blue-pale: #d8e4f1;
    --green: #6aa043;
    --green-pale: #e1ead9;
    --ink: #231f20;
    --white: #ffffff;
  }
  * { box-sizing: border-box; margin: 0; padding: 0; }
  html, body { width: 1200px; height: 568px; overflow: hidden; }
  body { background: var(--board); position: relative; font-family: "Montserrat", sans-serif; color: var(--ink); }

  .card { position: absolute; width: 272px; height: 156px; background: var(--card); overflow: hidden; box-shadow: 0 1px 2px rgba(0,0,0,.18); }
  .col-1 { left: 27px; } .col-2 { left: 314px; } .col-3 { left: 608px; } .col-4 { left: 893px; }
  .row-1 { top: 38px; } .row-2 { top: 210px; } .row-3 { top: 379px; }

  .abs { position: absolute; }

  /* Wordmark */
  .wordmark { position: absolute; display: flex; align-items: center; gap: 7px; }
  .wordmark-square { width: 14px; height: 14px; background: var(--blue); flex: none; }
  .wordmark-name { font-family: "Jost", sans-serif; font-weight: 500; color: var(--ink); line-height: 1.02; font-size: 17px; letter-spacing: .2px; }
  .wordmark.small .wordmark-square { width: 10px; height: 10px; }
  .wordmark.small .wordmark-name { font-size: 12px; }
  .wordmark.centered { left: 0; right: 0; top: 0; bottom: 0; justify-content: center; }

  /* Contact details */
  .person-name { position: absolute; font-family: "Saira Semi Condensed", sans-serif; font-weight: 600; font-size: 11px; line-height: 1.1; letter-spacing: .3px; text-transform: uppercase; white-space: nowrap; }
  .person-name.blue { color: var(--blue); }
  .person-name.light { color: var(--white); }
  .person-title { position: absolute; font-size: 5.4px; letter-spacing: 1.1px; text-transform: uppercase; font-weight: 500; display: flex; align-items: center; gap: 2px; white-space: nowrap; }
  .person-title .rule { display: block; height: .6px; background: var(--blue); flex: 1; }
  .title-badge { position: absolute; background: var(--green); color: var(--white); font-size: 5.4px; font-weight: 600; letter-spacing: 1.1px; padding: 3px 6px; text-transform: uppercase; white-space: nowrap; }
  .contact { position: absolute; display: flex; align-items: center; gap: 3px; font-size: 5.2px; font-weight: 600; white-space: nowrap; }
  .contact.phone { font-size: 6.6px; letter-spacing: .6px; }
  .contact svg { width: 9px; height: 9px; flex: none; }

  .brand-tint { position: absolute; }
</style>
</head>
<body>

<svg width="0" height="0" style="position:absolute">
  <defs>
    <symbol id="icon-phone" viewBox="0 0 20 20">
      <circle cx="10" cy="10" r="9" fill="none" stroke="#6aa043" stroke-width="1.6"/>
      <path d="M6.5 5.5l2 .2.8 2.3-1.2 1a6 6 0 0 0 2.9 2.9l1-1.2 2.3.8.2 2c-4.5.6-8.6-3.5-8-8z" fill="#6aa043"/>
    </symbol>
    <symbol id="icon-mail" viewBox="0 0 20 20">
      <circle cx="10" cy="10" r="9" fill="none" stroke="#6aa043" stroke-width="1.6"/>
      <rect x="5.2" y="6.6" width="9.6" height="6.8" fill="none" stroke="#6aa043" stroke-width="1.2"/>
      <path d="M5.2 6.6L10 10.6l4.8-4" fill="none" stroke="#6aa043" stroke-width="1.2"/>
    </symbol>
  </defs>
</svg>

<!-- Row 1 -->
<section class="card col-1 row-1">
  <div class="brand-tint" role="img" aria-label="Faint brand decoration" style="left:-6px;top:113px;width:56px;height:48px;background:var(--blue-pale);opacity:.7"></div>
  <div class="brand-tint" role="img" aria-label="Faint brand decoration" style="left:215px;top:0;width:57px;height:42px;background:linear-gradient(90deg,var(--blue-pale),var(--green-pale))"></div>
  <div class="wordmark centered"><span class="wordmark-square"></span><span class="wordmark-name">Graniteway<br>Surface Works</span></div>
</section>

<section class="card col-2 row-1">
  <div class="wordmark small" style="left:16px;top:44px"><span class="wordmark-square"></span><span class="wordmark-name">Graniteway<br>Surface Works</span></div>
  <div class="brand-tint" role="img" aria-label="Large brand decoration in blue and green" style="left:130px;top:13px;width:99px;height:97px;background:linear-gradient(180deg,var(--blue-pale) 0%,var(--blue-pale) 45%,var(--green-pale) 100%)"></div>
  <div class="person-name" style="left:140px;top:51px">Devon Halvorsen C.</div>
  <div class="person-title" style="left:141px;top:66px;right:0">Vice President<span class="rule"></span></div>
  <div class="contact phone" style="left:130px;top:117px"><svg><use href="#icon-phone"/></svg>708.214.5873</div>
  <div class="contact" style="left:130px;top:131px"><svg><use href="#icon-mail"/></svg>devon@granitewaysurfaceworks.example</div>
</section>

<section class="card col-3 row-1">
  <div class="wordmark centered"><span class="wordmark-square"></span><span class="wordmark-name">Graniteway<br>Surface Works</span></div>
</section>

<section class="card col-4 row-1">
  <div class="wordmark small" style="left:18px;top:62px"><span class="wordmark-square"></span><span class="wordmark-name">Graniteway<br>Surface Works</span></div>
  <svg class="abs" style="left:0;top:0" width="272" height="156" aria-hidden="true">
    <path d="M140 33V11H262V142H140V108" fill="none" stroke="var(--blue)" stroke-width="6"/>
  </svg>
  <div class="person-name blue" style="left:137px;top:44px;font-size:10.5px">Morgan Prescoe C.</div>
  <div class="title-badge" style="left:138px;top:61px">President</div>
  <div class="contact phone" style="left:138px;top:79px"><svg><use href="#icon-phone"/></svg>708.389.6145</div>
  <div class="contact" style="left:138px;top:92px;font-size:4.6px;gap:2px"><svg style="width:8px;height:8px"><use href="#icon-mail"/></svg>morgan@granitewaysurfaceworks.example</div>
</section>

<!-- Row 2 -->
<section class="card col-1 row-2">
  <div class="wordmark centered"><span class="wordmark-square"></span><span class="wordmark-name">Graniteway<br>Surface Works</span></div>
</section>

<section class="card col-2 row-2">
  <div class="wordmark small" style="left:22px;top:62px"><span class="wordmark-square"></span><span class="wordmark-name">Graniteway<br>Surface Works</span></div>
  <div class="person-name blue" style="left:128px;top:46px;font-size:12.5px">Bo Vu C.</div>
  <div class="person-title" style="left:131px;top:66px;width:124px">Managing Partner<span class="rule"></span></div>
  <div class="contact phone" style="left:130px;top:80px"><svg><use href="#icon-phone"/></svg>405.631.8207</div>
  <div class="contact" style="left:130px;top:96px;font-size:6px"><svg><use href="#icon-mail"/></svg>bo@granitewaysurfaceworks.example</div>
  <div class="abs" style="left:269px;top:44px;width:3px;height:19px;background:var(--green)"></div>
</section>

<section class="card col-3 row-2">
  <div class="brand-tint" role="img" aria-label="Repeating faint brand pattern" style="inset:0;background:linear-gradient(135deg,#e9eef5,#eef2ea)"></div>
  <div class="wordmark" style="left:20px;top:72px"><span class="wordmark-square"></span><span class="wordmark-name">Graniteway<br>Surface Works</span></div>
</section>

<section class="card col-4 row-2">
  <div class="brand-tint" role="img" aria-label="Blue band with brand pattern" style="left:0;top:0;width:272px;height:70px;background:var(--blue)"></div>
  <div class="abs" style="left:0;top:30px;width:2px;height:17px;background:var(--green)"></div>
  <div class="person-name light" style="left:13px;top:27px;font-size:11.5px">Devon Halvorsen C.</div>
  <div class="person-title" style="left:14px;top:44px;color:var(--white)">Vice President</div>
  <div class="contact phone" style="left:13px;top:80px"><svg><use href="#icon-phone"/></svg>708.214.5873</div>
  <div class="contact" style="left:13px;top:95px;font-size:5px"><svg><use href="#icon-mail"/></svg>devon@granitewaysurfaceworks.example</div>
  <div class="abs" style="left:150px;top:26px;width:114px;height:111px;background:var(--white)">
    <div class="wordmark small centered"><span class="wordmark-square"></span><span class="wordmark-name">Graniteway<br>Surface Works</span></div>
  </div>
</section>

<!-- Row 3 -->
<section class="card col-1 row-3">
  <div class="brand-tint" role="img" aria-label="Faint large brand decoration" style="left:150px;top:0;width:122px;height:156px;background:linear-gradient(120deg,var(--blue-pale),var(--green-pale));opacity:.8;clip-path:polygon(50% 0,100% 0,100% 100%,50% 100%,0 50%)"></div>
  <div class="wordmark" style="left:22px;top:60px"><span class="wordmark-square"></span><span class="wordmark-name">Graniteway<br>Surface Works</span></div>
</section>

<section class="card col-2 row-3">
  <div class="wordmark small" style="left:14px;top:18px"><span class="wordmark-square"></span><span class="wordmark-name">Graniteway<br>Surface Works</span></div>
  <div class="abs" style="left:0;top:84px;width:3px;height:16px;background:var(--blue)"></div>
  <div class="person-name" style="left:12px;top:81px;font-size:11px">Morgan Prescoe C.</div>
  <div class="person-title" style="left:13px;top:97px;width:92px;color:var(--blue)">President</div>
  <div class="abs" style="left:13px;top:105px;width:92px;height:.6px;background:var(--blue-pale)"></div>
  <div class="contact phone" style="left:12px;top:118px"><svg><use href="#icon-phone"/></svg>708.389.6145</div>
  <div class="contact" style="left:12px;top:132px;font-size:5px"><svg><use href="#icon-mail"/></svg>morgan@granitewaysurfaceworks.example</div>
  <div class="brand-tint" role="img" aria-label="Large brand decoration in blue and green" style="left:150px;top:0;width:122px;height:156px;background:linear-gradient(120deg,var(--blue) 0%,#3f82bd 50%,var(--green) 100%);opacity:.9;clip-path:polygon(50% 0,100% 0,100% 100%,50% 100%,0 47%)"></div>
</section>

</body>
</html>
```